Pest Control Company needs business card!

Hi there, we need a business card designed for our new Pest Control Company. Ideally this card will be simple, yet feel elegant and high end. We want to use the colours Orange, Black and White. Please see our attached logo for the exact colours.

Business card details:

Phone - 0461 275 804
Name - Gavin Holloway
Email - Info@steadfastverminguard.com.au

We would also like to include the following list with dot points:

SERVICES / INSPECTIONS

Termites, Wood Borers, Ants, Cockroaches, Spiders, Fleas, Mice, Rats, Bed Bugs, & More!

```html
<!DOCTYPE html>
<html lang="en">
<head>
<meta charset="utf-8">
<title>Steadfast Vermin Guard – Business Card</title>
<link href="https://fonts.googleapis.com/css2?family=Montserrat:wght@400;500;700;800&display=swap" rel="stylesheet">
<style>
  :root {
    --orange: #f2801f;
    --black: #141414;
    --ink: #1c1c1c;
    --white: #ffffff;
    --backdrop: #2b2b2b;
  }
  * { box-sizing: border-box; margin: 0; padding: 0; }
  html, body {
    width: 1200px; height: 1000px; overflow: hidden;
    background: var(--backdrop);
    font-family: "Montserrat", sans-serif;
  }
  .sheet {
    width: 1200px; height: 1000px;
    display: flex; flex-direction: column; align-items: center; justify-content: center;
    gap: 36px;
  }
  .card {
    width: 800px; height: 457px;
    position: relative;
    border-radius: 4px;
    overflow: hidden;
  }
  /* Back side */
  .card--back {
    background: var(--black);
    color: var(--white);
    display: flex; flex-direction: column; align-items: center; justify-content: center;
    text-align: center;
  }
  .brand {
    display: flex; align-items: center; gap: 16px;
    font-weight: 800; font-size: 44px; line-height: 1; letter-spacing: -0.5px;
    text-transform: uppercase;
  }
  .brand__dot {
    width: 22px; height: 22px; border-radius: 50%;
    background: currentColor; flex: none;
  }
  .card--back .brand { color: var(--orange); margin-bottom: 48px; }
  .services__title {
    color: var(--orange); font-weight: 700; font-size: 17px; letter-spacing: 0.5px;
    margin-bottom: 12px;
  }
  .services__list {
    list-style: none; display: flex; flex-wrap: wrap; justify-content: center;
    max-width: 640px; row-gap: 6px;
    font-size: 17px; font-weight: 500;
  }
  .services__list li { display: flex; align-items: center; margin: 0 7px; }
  .services__list li::before {
    content: ""; width: 7px; height: 7px; border-radius: 50%;
    background: var(--orange); margin-right: 7px;
  }
  /* Front side */
  .card--front {
    background: var(--white);
    color: var(--ink);
    padding: 56px 64px;
  }
  .card--front .brand { color: var(--ink); font-size: 38px; }
  .person {
    margin-top: 58px;
    color: var(--orange); font-weight: 800; font-size: 30px; letter-spacing: 0.3px;
    text-transform: uppercase;
  }
  .person__rule {
    width: 34px; height: 3px; background: var(--orange);
    margin: 16px 0 18px;
  }
  .contact { list-style: none; display: flex; flex-direction: column; gap: 8px; }
  .contact li { display: flex; align-items: center; gap: 14px; font-size: 20px; }
  .contact svg { width: 20px; height: 20px; fill: var(--orange); flex: none; }
</style>
</head>
<body>
<main class="sheet">

  <section class="card card--back" aria-label="Card back">
    <div class="brand"><span class="brand__dot"></span>Steadfast Vermin Guard</div>
    <h2 class="services__title">SERVICES / INSPECTIONS</h2>
    <ul class="services__list">
      <li>Termites</li><li>Wood Borers</li><li>Ants</li><li>Cockroaches</li>
      <li>Spiders</li><li>Fleas</li><li>Mice</li><li>Rats</li><li>Bed Bugs</li><li>&amp; More!</li>
    </ul>
  </section>

  <section class="card card--front" aria-label="Card front">
    <div class="brand"><span class="brand__dot"></span>Steadfast Vermin Guard</div>
    <h1 class="person">Gavin Holloway</h1>
    <div class="person__rule"></div>
    <ul class="contact">
      <li>
        <svg viewBox="0 0 24 24" aria-hidden="true"><path d="M6.6 10.8a15.1 15.1 0 0 0 6.6 6.6l2.2-2.2c.3-.3.7-.4 1-.2 1.1.4 2.3.6 3.6.6.6 0 1 .4 1 1V20c0 .6-.4 1-1 1A17 17 0 0 1 3 4c0-.6.4-1 1-1h3.5c.6 0 1 .4 1 1 0 1.3.2 2.5.6 3.6.1.3 0 .7-.2 1z"/></svg>
        0461 275 804
      </li>
      <li>
        <svg viewBox="0 0 24 24" aria-hidden="true"><path d="M2 5h20v14H2zm2 2v.5l8 5 8-5V7l-8 5z"/></svg>
        Info@steadfastverminguard.com.au
      </li>
      <li>
        <svg viewBox="0 0 24 24" aria-hidden="true"><path d="M12 2a10 10 0 1 0 0 20 10 10 0 0 0 0-20zm-1 17.9A8 8 0 0 1 4.1 10L9 15v1c0 1.1.9 2 2 2zm6.9-2.5A2 2 0 0 0 16 16h-1v-3a1 1 0 0 0-1-1H8v-2h2a1 1 0 0 0 1-1V7h2a2 2 0 0 0 2-2v-.4a8 8 0 0 1 2.9 12.8z"/></svg>
        www.steadfastverminguard.com.au
      </li>
    </ul>
  </section>

</main>
</body>
</html>
```